Green Logistics / Last Mile Delivery Firm needs cool one-page website

FYI - We do have a detailed brief in the uploaded files section below
COMPANY
We recently launched the company Quillby Logistics which is a pioneer in urban green logistics and provides zero-emissions last mile delivery services (i.e. delivery of parcels with delivery vans to the doorstep of households) for its logistics and retail clients.
We take on urban parcel delivery for our clients with a 100% electric commercial vehicles fleet, fair and sustainable working conditions for our employees and an unparalleled professional and customer-focused mindset.
WEBSITE
In the detailed brief, we have provided examples to emulate. We need the design + coding of the website. Website needs to be friendly/optimized for and should open swiftly on both Android & iOS.
In general, the website should convey
- green mission of the company
- sustainability (good working conditions, focus on employees)
- customer orientation
- professionalism
DESIGN
In the detailed brief, we have provided designs to emulate.
Color design: we do have a logo which features 2 green colors (one lighter and one darker color tone). However, the colors on the website do not necessarily need to follow these 2 colors exactly as we are able to switch the logo colors.
Imagery: should reflect maybe 50% green/leaf/tree , 25% customer and employee orientation, and 25% logistics (here it's important that it is the last mile delivery, i.e. delivery with delivery vans to the doorstep of households)

```html
<!DOCTYPE html>
<html lang="en">
<head>
<meta charset="utf-8">
<title>Quillby Logistics – Sustainable Last Mile</title>
<link rel="stylesheet" href="https://fonts.googleapis.com/css2?family=Oswald:wght@400;500&family=Roboto:wght@400;500;700&display=swap">
<style>
:root{
  --green:#3aa935;
  --green-dark:#1f7a33;
  --green-light:#8cc63f;
  --text:#555;
  --heading:#1d1d1d;
  --line:#e3e3e3;
  --bg-soft:#f4f4f4;
  --white:#fff;
}
*{box-sizing:border-box;margin:0;padding:0}
html,body{width:1200px;height:5240px;overflow:hidden}
body{font-family:"Roboto",Arial,sans-serif;color:var(--text);background:var(--white);position:relative}
.abs{position:absolute}
.section{position:absolute;left:0;width:1200px}
.heading{font-family:"Oswald",Arial,sans-serif;font-weight:500;color:var(--heading);text-transform:uppercase;text-align:center;font-size:40px;letter-spacing:-.5px}
.heading-rule{width:38px;height:3px;background:var(--green);margin:10px auto 0}
.btn{position:absolute;display:flex;align-items:center;justify-content:center;background:var(--green);color:var(--white);font-weight:700;font-size:15px;border-radius:26px;text-transform:uppercase}

/* header & hero */
.hero{top:0;height:602px;background:linear-gradient(180deg,#2d4a2c 0%,#3f6a36 40%,#2a4c29 100%)}
.hero-art{position:absolute;inset:0;background:radial-gradient(ellipse at 45% 55%,#6f8a62 0,#41663a 30%,#23402a 80%)}
.topbar-line{position:absolute;left:0;right:0;top:104px;height:1px;background:rgba(255,255,255,.25)}
.brand{position:absolute;left:112px;top:32px;display:flex;align-items:center;gap:12px;font-family:"Roboto",sans-serif;font-weight:700;font-size:28px;color:var(--green-light)}
.brand-dot{width:40px;height:40px;border-radius:50%;background:var(--green-light)}
.contact-item{position:absolute;top:14px;display:flex;align-items:center;gap:10px;color:var(--white)}
.contact-item small{display:block;font-size:11px}
.contact-item b{font-size:18px;font-weight:500}
.ic-round{width:36px;height:36px;border-radius:50%;border:2px solid var(--white);display:flex;align-items:center;justify-content:center}
.flag{position:absolute;left:1048px;top:14px;width:40px;height:40px;border-radius:50%;background:linear-gradient(180deg,#c33 0 14%,#fff 14% 28%,#c33 28% 42%,#fff 42% 56%,#c33 56% 70%,#fff 70% 84%,#c33 84%);overflow:hidden}
.flag::after{content:"";position:absolute;left:0;top:0;width:20px;height:20px;background:#2f3b8f}
.nav a{position:absolute;top:74px;color:var(--white);font-size:16px;text-decoration:none}
.nav a.active{color:var(--green-light)}
.hero-title{position:absolute;top:262px;width:100%;text-align:center;font-family:"Oswald",sans-serif;font-size:42px;color:var(--white);letter-spacing:-.5px}
.hero-sub{position:absolute;top:320px;width:100%;text-align:center;font-size:21px;color:var(--white)}
.arrow{position:absolute;top:318px}
.dots{position:absolute;top:568px;left:530px;display:flex;gap:8px}
.dots span{width:22px;height:3px;background:rgba(255,255,255,.4)}
.dots span.on{background:var(--white)}

/* about */
.about{top:602px;height:757px;background:var(--bg-soft)}
.lead{position:absolute;left:200px;width:800px;text-align:center;font-size:14.5px;line-height:26px;color:#444}
.card{position:absolute;top:232px;width:316px;height:447px;background:var(--white);box-shadow:0 2px 8px rgba(0,0,0,.12);text-align:center}
.card-img{height:213px}
.card-badge{position:absolute;left:126px;top:174px;width:64px;height:64px;border-radius:50%;background:var(--green);border:4px solid var(--white);display:flex;align-items:center;justify-content:center}
.card h3{margin-top:50px;font-size:23px;font-weight:700;color:#111}
.card p{margin:14px 22px 0;text-align:justify;font-size:12.5px;line-height:24px;color:#666}
.card .more{position:absolute;bottom:20px;width:100%;color:var(--green);font-weight:700;font-size:15px}

/* is / is not */
.compare{top:1359px;height:579px}
.half{position:absolute;top:0;height:579px;width:600px}
.half-left{left:0;background:linear-gradient(180deg,#d9ecf3 0%,#b9d9e6 55%,#8fa8b1 100%)}
.half-right{left:600px;background:linear-gradient(180deg,#6fcbef 0%,#9ddcf4 55%,#73b851 100%)}
.compare-title{position:absolute;left:112px;top:62px;display:flex;align-items:center;gap:10px;font-family:"Oswald",sans-serif;font-size:38px;color:var(--green-dark)}
.compare-title i{width:6px;height:46px;background:var(--green-dark)}
.list{position:absolute;font-size:15px;color:#222}
.list h4{font-size:15px;font-weight:500;margin-bottom:10px}
.list li{list-style:none;line-height:34px;padding-left:20px;position:relative}
.list li::before{content:"";position:absolute;left:0;top:13px;width:9px;height:9px;border-radius:50%;background:var(--green)}
.list.no h4,.list.no li{text-decoration:line-through}
.list.yes h4{color:#1d7b32}

/* services */
.services{top:1938px;height:605px}
.svc{position:absolute;top:265px;width:236px;height:254px;background:var(--white);box-shadow:0 1px 6px rgba(0,0,0,.15);text-align:center}
.svc-icon{width:76px;height:76px;border-radius:50%;border:4px solid var(--green-light);margin:22px auto 0;display:flex;align-items:center;justify-content:center}
.svc h4{margin:18px 10px 0;font-size:15px;font-weight:500;color:#222;line-height:22px}
.svc p{margin:8px 24px 0;font-size:12.5px;line-height:24px;color:#777}

/* touch */
.touch{top:2543px;height:366px;background:linear-gradient(120deg,#143a1f 0%,#21502a 50%,#15361d 100%)}
.touch h2{position:absolute;left:112px;top:120px;font-family:"Oswald",sans-serif;font-weight:500;font-size:36px;color:var(--white)}
.touch p{position:absolute;left:112px;top:182px;width:740px;font-size:14.5px;line-height:27px;color:var(--white)}

/* careers */
.careers{top:2909px;height:874px}
.career-art{position:absolute;left:122px;top:142px;width:356px;height:326px;border-radius:50%;background:radial-gradient(circle at 40% 40%,#8cc63f,#3aa935 60%,#1f7a33)}
.career-text{position:absolute;left:508px;top:150px;width:566px;font-size:13.4px;line-height:26.4px;color:#555;text-align:justify}
.acc{position:absolute;left:126px;width:946px;height:88px;display:flex;align-items:center;gap:24px;border-bottom:1px solid var(--line);font-size:17px;font-weight:500;color:#222}
.acc-plus{width:44px;height:44px;border-radius:50%;background:var(--white);box-shadow:0 1px 5px rgba(0,0,0,.18);display:flex;align-items:center;justify-content:center}

/* contact */
.contact{top:3783px;height:957px}
.contact h2{position:absolute;left:110px;top:38px;font-family:"Oswald",sans-serif;font-weight:500;font-size:40px;color:var(--heading)}
.contact .intro{position:absolute;left:110px;top:100px;width:950px;font-size:14px;line-height:29px;color:#555}
.map{position:absolute;left:0;top:175px;width:1200px;height:395px;background:linear-gradient(135deg,#eef0ec,#e4e7e2 50%,#ecefe8)}
.map-card{position:absolute;left:133px;top:65px;width:225px;height:138px;background:var(--white);box-shadow:0 2px 8px rgba(0,0,0,.2);padding:70px 0 0 20px;font-size:13px;color:#222;line-height:19px}
.map-card .stars{color:#f2b300;font-size:13px;letter-spacing:1px}
.info{position:absolute;left:134px;display:flex;gap:16px;color:#222}
.info b{font-size:20px;font-weight:400;display:block}
.info span{font-size:13px;line-height:21px}
.field{position:absolute;border:1px solid #ddd;background:var(--white);font-size:13px;color:#666;padding:14px 18px}

/* footer */
.footer{top:4740px;height:500px;background:linear-gradient(180deg,#ffffff 0%,#a5c98b 25%,#3d7a2c 55%,#1c3b16 100%)}
.footer-brand{position:absolute;top:200px;width:100%;text-align:center;color:var(--white);font-weight:700;font-size:28px}
.footer-brand .dot{display:block;width:70px;height:70px;border-radius:50%;background:var(--white);margin:0 auto 14px}
.footer-nav{position:absolute;top:343px;width:100%;display:flex;justify-content:center;gap:70px;color:var(--white);font-weight:700;font-size:16px}
.socials{position:absolute;top:402px;left:525px;display:flex;gap:14px}
.socials span{width:36px;height:36px;border-radius:50%;background:var(--green-light)}
.copy{position:absolute;top:455px;width:100%;text-align:center;color:var(--white);font-size:12px}
</style>
</head>
<body>

<header class="section hero">
  <div class="hero-art" role="img" aria-label="Aerial photo of an electric delivery van on a road through green forest"></div>
  <div class="brand"><span class="brand-dot"></span>QUILLBY LOGISTICS</div>
  <div class="contact-item" style="left:592px">
    <span class="ic-round"><svg width="16" height="16" viewBox="0 0 24 24" fill="#fff"><path d="M6.6 10.8a15 15 0 0 0 6.6 6.6l2.2-2.2a1 1 0 0 1 1-.25 11.4 11.4 0 0 0 3.6.57 1 1 0 0 1 1 1V20a1 1 0 0 1-1 1A17 17 0 0 1 3 4a1 1 0 0 1 1-1h3.5a1 1 0 0 1 1 1c0 1.25.2 2.45.57 3.57a1 1 0 0 1-.25 1z"/></svg></span>
    <div><small>Call Now</small><b>888.888.8888</b></div>
  </div>
  <div class="contact-item" style="left:785px">
    <span class="ic-round"><svg width="16" height="12" viewBox="0 0 16 12" fill="none" stroke="#fff" stroke-width="1.6"><rect x="1" y="1" width="14" height="10"/><path d="M1 1l7 6 7-6"/></svg></span>
    <div><small>Email</small><b>info@quillbylogistics.com</b></div>
  </div>
  <div class="flag" aria-label="Language: English"></div>
  <div class="topbar-line"></div>
  <nav class="nav">
    <a class="active" style="left:500px">Home</a>
    <a style="left:625px">About</a>
    <a style="left:748px">Services</a>
    <a style="left:888px">Careers</a>
    <a style="left:1026px">Contact</a>
  </nav>
  <svg class="arrow" style="left:72px" width="18" height="30" viewBox="0 0 18 30" fill="none" stroke="#fff" stroke-width="2"><path d="M16 2L3 15l13 13"/></svg>
  <svg class="arrow" style="left:1110px" width="18" height="30" viewBox="0 0 18 30" fill="none" stroke="#fff" stroke-width="2"><path d="M2 2l13 13L2 28"/></svg>
  <h1 class="hero-title">QUILLBY LOGISTICS – SUSTAINABLE LAST MILE</h1>
  <p class="hero-sub">Because we care about trees!</p>
  <div class="btn" style="left:510px;top:370px;width:180px;height:46px">Get Started</div>
  <div class="dots"><span></span><span class="on"></span><span></span><span></span><span></span></div>
</header>

<section class="section about">
  <h2 class="heading" style="margin-top:76px">About Us</h2>
  <div class="heading-rule"></div>
  <p class="lead" style="top:154px">Lorem ipsum dolor sit amet, consectetur adipiscing elit, sed do eiusmod tempor incidmagna aliqua. Quis ipsum suspendisse ultrices gravida. Risus commodo viverra maecenas accumsan lacus vel facilisis.</p>

  <article class="card" style="left:110px">
    <div class="card-img" role="img" aria-label="Green delivery truck made of plants" style="background:linear-gradient(135deg,#e7ebe4,#b6d79a 60%,#dfe6dc)"></div>
    <div class="card-badge"><svg width="30" height="30" viewBox="0 0 30 30" fill="none" stroke="#fff" stroke-width="2"><rect x="5" y="6" width="20" height="18" rx="2"/><path d="M9 12h12M9 17h8"/></svg></div>
    <h3>WHO WE ARE</h3>
    <p>Quillby Logistics is a pioneer in urban green logistics and provides zeroemissions last mile delivery services for its logistics and retail clients.</p>
    <div class="more">LOAD MORE ⌄</div>
  </article>
  <article class="card" style="left:441px">
    <div class="card-img" role="img" aria-label="Team hands holding a young plant together" style="background:linear-gradient(135deg,#5a4636,#8a6a4f 50%,#3e3027)"></div>
    <div class="card-badge"><svg width="30" height="30" viewBox="0 0 30 30" fill="none" stroke="#fff" stroke-width="2"><circle cx="15" cy="15" r="10"/><circle cx="15" cy="15" r="5"/><circle cx="15" cy="15" r="1" fill="#fff"/></svg></div>
    <h3>OUR MISSION</h3>
    <p>To satisfy consumers' ever-rising desire to buy products online, the CO2 emissions from delivery traffic will increase by 32% in the top 100 cities globally until 2030.</p>
    <div class="more">LOAD MORE ⌄</div>
  </article>
  <article class="card" style="left:773px">
    <div class="card-img" role="img" aria-label="Jars of coins with plants growing" style="background:linear-gradient(135deg,#2f4a22,#7ba94a 55%,#c9d98a)"></div>
    <div class="card-badge"><svg width="30" height="30" viewBox="0 0 30 30" fill="none" stroke="#fff" stroke-width="2"><path d="M6 12l4-5h10l4 5-9 11z"/><path d="M6 12h18"/></svg></div>
    <h3>OUR VALUES</h3>
    <p>We see ourselves as a professional services company who strongly cares about the environment, its clients and their customers, as well as its employees.</p>
    <div class="more">LOAD MORE ⌄</div>
  </article>
</section>

<section class="section compare">
  <div class="half half-left" role="img" aria-label="Grey city skyline with an ordinary diesel truck"></div>
  <div class="half half-right" role="img" aria-label="Bright city skyline with a green electric van and a courier"></div>
  <div class="compare-title"><i></i>QUILLBY LOGISTICS IS...</div>
  <div class="list no" style="left:256px;top:140px">
    <h4>AN ORDINARY PARCEL DELIVERY FIRM</h4>
    <ul>
      <li>Polluting our cities</li>
      <li>Always in a rush</li>
      <li>Short-term oriented</li>
      <li>Focusing on profit only</li>
      <li>Yet another parcel delivery firm</li>
    </ul>
  </div>
  <div class="list yes" style="left:628px;top:140px">
    <h4>A PIONEERING GREEN LAST MILE</h4>
    <ul>
      <li>Delivering parcels emissions-free</li>
      <li>Putting customer experience first</li>
      <li>Operating the business sustainably</li>
      <li>Focusing on the environment, customers and employees</li>
      <li>A professional services company</li>
    </ul>
  </div>
</section>

<section class="section services">
  <h2 class="heading" style="margin-top:78px">Our Services</h2>
  <div class="heading-rule"></div>
  <p class="lead" style="top:156px;left:196px;width:808px">Quillby Logistics provides last mile delivery services in urban areas to clients in the logistics and retail space. Our permanent employees are all highly trained and commit to highest professional standards which we continuously review and further develop with them.</p>

  <div class="svc" style="left:110px">
    <div class="svc-icon"><svg width="36" height="36" viewBox="0 0 36 36" fill="none" stroke="#3aa935" stroke-width="2"><circle cx="18" cy="14" r="8"/><path d="M18 22v10M12 32h12"/></svg></div>
    <h4>Zero-emission delivery</h4>
    <p>We live a customer-oriented mindset, always measuring ourselves against their experience</p>
  </div>
  <div class="svc" style="left:356px">
    <div class="svc-icon"><svg width="36" height="36" viewBox="0 0 36 36" fill="none" stroke="#3aa935" stroke-width="2"><circle cx="18" cy="11" r="5"/><path d="M8 31c0-6 4-10 10-10s10 4 10 10z"/></svg></div>
    <h4>Highly trained delivery drivers</h4>
    <p>We only employ permanently, train far above average, and live a great team spirit</p>
  </div>
  <div class="svc" style="left:604px">
    <div class="svc-icon"><svg width="36" height="36" viewBox="0 0 36 36" fill="none" stroke="#3aa935" stroke-width="2"><circle cx="18" cy="18" r="12"/><path d="M6 18h24M18 6c-6 6-6 18 0 24M18 6c6 6 6 18 0 24"/></svg></div>
    <h4>Professional all around</h4>
    <p>We honor our commitments and hold ourselves to the highest professional standards</p>
  </div>
  <div class="svc" style="left:850px">
    <div class="svc-icon"><svg width="36" height="36" viewBox="0 0 36 36" fill="none" stroke="#3aa935" stroke-width="2"><circle cx="11" cy="12" r="4"/><circle cx="25" cy="12" r="4"/><circle cx="18" cy="16" r="4"/><path d="M5 30c0-5 3-9 6-9M31 30c0-5-3-9-6-9M11 31c0-5 3-8 7-8s7 3 7 8"/></svg></div>
    <h4>Unparalleled customer focus</h4>
    <p>We live a customer-oriented mindset, always measuring ourselves against their experience</p>
  </div>
</section>

<section class="section touch" role="img" aria-label="Aerial photo of a dark green forest with a road">
  <h2>GET IN TOUCH WITH QUILLBY LOGISTICS</h2>
  <p>If you got excited, or have a question about our services, our approach, our jobs or just want to get in touch to chat about how green logistics can make the planet a little bit better, please get in touch!</p>
  <div class="btn" style="left:905px;top:179px;width:180px;height:50px">Contact Us</div>
</section>

<section class="section careers">
  <h2 class="heading" style="margin-top:60px">Careers</h2>
  <div class="heading-rule"></div>
  <div class="career-art" role="img" aria-label="Large green leaf-heart illustration"></div>
  <p class="career-text">If you join Quillby Logistics, you join a family. We elevate one another, care for each other's wellbeing and growth, and celebrate our successes. We strongly believe growth is a team sport and that every member of the family fully contributes to the achievements of the company overall. At the heart of everything we do at Quillby Logistics is a relentless focus on our mission. That's why we aim to ensure our employees can follow their own passion at the workplace, be this working in a truly collaborative and caring team, putting a smile on a customer's face or making the world a better place. While we are helping our clients grow by delivering their parcels, we are also helping all our employees grow personally and professionally. We care about our employees' happiness and wellbeing which is why we provide additional benefits like supplementary health insurance. If you are excited about joining our Quillby Logistics family, please check out our open positions</p>
  <div class="acc" style="top:491px"><span class="acc-plus"><svg width="18" height="18" stroke="#333" stroke-width="2"><path d="M9 2v14M2 9h14"/></svg></span>Full-time driver / parcel deliverer (m/f/d) for Berlin</div>
  <div class="acc" style="top:579px"><span class="acc-plus"><svg width="18" height="18" stroke="#333" stroke-width="2"><path d="M9 2v14M2 9h14"/></svg></span>Your tasks as a delivery driver:</div>
  <div class="acc" style="top:668px"><span class="acc-plus"><svg width="18" height="18" stroke="#333" stroke-width="2"><path d="M9 2v14M2 9h14"/></svg></span>Required knowledge and skills</div>
  <div class="acc" style="top:756px"><span class="acc-plus"><svg width="18" height="18" stroke="#333" stroke-width="2"><path d="M9 2v14M2 9h14"/></svg></span>What you can expected from the Quillby Logistics family:</div>
</section>

<section class="section contact">
  <h2>CONTACT</h2>
  <p class="intro">We'd love to hear from you! Whether you have a question about our services, our approach, our jobs or just want to get in touch to chat about how green logistics can make the planet a little bit better, our team is ready to answer your questions and enquiries.</p>
  <div class="map" role="img" aria-label="Street map of the office location">
    <div class="map-card">1234 Somestreet Anywhere<br>USA 21212<br><span class="stars">★★★★★</span></div>
  </div>

  <div class="info" style="top:608px">
    <svg width="30" height="34" viewBox="0 0 30 34" fill="none" stroke="#3aa935" stroke-width="2"><path d="M15 32s11-11 11-19a11 11 0 0 0-22 0c0 8 11 19 11 19z"/><circle cx="15" cy="13" r="4"/></svg>
    <div><b>Location:</b><span>1234 Somestreet Anywhere USA<br>21212</span></div>
  </div>
  <div class="info" style="top:700px">
    <svg width="34" height="24" viewBox="0 0 34 24" fill="none" stroke="#3aa935" stroke-width="2"><rect x="1" y="1" width="32" height="22"/><path d="M1 1l16 13L33 1"/></svg>
    <div><b>Email:</b><span>info@quillbylogistics.com</span></div>
  </div>
  <div class="info" style="top:770px">
    <svg width="32" height="32" viewBox="0 0 24 24" fill="none" stroke="#3aa935" stroke-width="1.5"><path d="M6.6 10.8a15 15 0 0 0 6.6 6.6l2.2-2.2a1 1 0 0 1 1-.25 11.4 11.4 0 0 0 3.6.57 1 1 0 0 1 1 1V20a1 1 0 0 1-1 1A17 17 0 0 1 3 4a1 1 0 0 1 1-1h3.5a1 1 0 0 1 1 1c0 1.25.2 2.45.57 3.57a1 1 0 0 1-.25 1z"/></svg>
    <div><b>Call:</b><span>888 - 888 - 8888</span></div>
  </div>

  <div class="field" style="left:478px;top:615px;width:286px;height:46px">Your Name</div>
  <div class="field" style="left:774px;top:615px;width:286px;height:46px">Your Email</div>
  <div class="field" style="left:478px;top:671px;width:582px;height:46px">Subject</div>
  <div class="field" style="left:478px;top:729px;width:582px;height:106px">Message</div>
  <div class="btn" style="left:685px;top:850px;width:170px;height:46px">Send Message</div>
</section>

<footer class="section footer" role="img" aria-label="Close-up photo of green grass in sunlight">
  <div class="footer-brand"><span class="dot"></span>QUILLBY LOGISTICS</div>
  <div class="footer-nav"><span>HOME</span><span>ABOUT</span><span>SERVICES</span><span>CAREERS</span><span>CONTACT</span></div>
  <div class="socials"><span></span><span></span><span></span></div>
  <p class="copy">© 2020 Quillby Logistics &nbsp; | &nbsp; Legal Notice &nbsp; | &nbsp; Privacy Policy</p>
</footer>

</body>
</html>
```